Palm Crest Engineering Consulting & Training Co., LTD.
Palm Crest
Use standard fonts
Arch. Salim Fathi Benzoura
General Manager
Sawani- Algharbia, District - Tripoli, Libya
palmcrest@mailvane.net
The Arabic company name and address نخيل الساحل للاستشارات والخدمات الهندسية والتدريب ذ.م.م الغربية السواني - طرابلس , ليبيا
The Arabic name and information م. سالم الفتحي بنزورة المدير العام
Brisk Brisk
Ok. Can u give some star rating please. Stationary will be based on business card.
kelvurn kelvurn
I'm ordering Business Cards and Stationery kit :(

```html
<!DOCTYPE html>
<html lang="en">
<head>
<meta charset="utf-8">
<title>Palm Crest Business Card</title>
<link href="https://fonts.googleapis.com/css2?family=Cinzel:wght@600&family=Open+Sans:wght@400;600;700&family=Cairo:wght@400;600;700&display=swap" rel="stylesheet">
<style>
  :root {
    --stage: #2a2a2c;
    --brand-red: #9a1419;
    --brand-red-dark: #6e0c10;
    --paper: #f5f5f5;
    --ink: #3a3a3a;
    --white: #ffffff;
    --muted: #d9b7b8;
  }
  * { box-sizing: border-box; margin: 0; padding: 0; }
  html, body { width: 1200px; height: 904px; overflow: hidden; }
  body {
    background: var(--stage);
    font-family: "Open Sans", Arial, sans-serif;
    position: relative;
  }
  .card {
    position: absolute;
    left: 250px;
    width: 700px;
    height: 400px;
    border-radius: 4px;
    overflow: hidden;
  }
  .card--front {
    top: 30px;
    background: radial-gradient(ellipse at 50% 40%, var(--brand-red) 0%, var(--brand-red-dark) 100%);
    display: flex; align-items: center; justify-content: center;
  }
  .card--back { top: 474px; background: var(--paper); }

  .brand {
    display: flex; align-items: center; gap: 14px;
    font-family: "Cinzel", Georgia, serif;
    font-weight: 600;
  }
  .brand__mark { width: 22px; height: 22px; border-radius: 50%; }
  .card--front .brand { color: var(--white); font-size: 58px; }
  .card--front .brand__mark { background: var(--white); }

  .back__logo {
    height: 190px;
    display: flex; align-items: center; justify-content: center;
  }
  .card--back .brand { color: var(--brand-red); font-size: 50px; }
  .card--back .brand__mark { background: var(--brand-red); width: 20px; height: 20px; }

  .back__band {
    position: absolute; left: 0; top: 190px;
    width: 100%; height: 150px;
    background: linear-gradient(180deg, var(--brand-red) 0%, var(--brand-red-dark) 100%);
    color: var(--white);
    display: flex; align-items: center;
  }
  .band__arabic {
    flex: 1; padding: 0 28px 0 30px;
    font-family: "Cairo", Tahoma, sans-serif;
    direction: rtl; text-align: right;
    font-size: 12.5px; line-height: 1.6;
  }
  .band__arabic .person { font-size: 17px; font-weight: 700; }
  .band__divider { width: 1px; height: 96px; background: var(--muted); }
  .band__english {
    flex: 1; padding: 0 30px 0 28px;
    font-size: 12.5px; line-height: 1.6;
  }
  .band__english .person { font-size: 17px; font-weight: 700; }

  .back__contacts {
    position: absolute; left: 0; bottom: 0;
    width: 100%; height: 60px;
    display: flex; align-items: center; justify-content: space-between;
    padding: 0 34px;
    color: var(--ink); font-size: 13px;
  }
  .contact { display: flex; align-items: center; gap: 8px; }
  .contact__icon { width: 16px; height: 16px; fill: var(--brand-red); }
  .contact__sep { width: 1px; height: 20px; background: #bdbdbd; }
</style>
</head>
<body>
  <section class="card card--front" aria-label="Business card front">
    <div class="brand"><span class="brand__mark"></span><span>Palm Crest</span></div>
  </section>

  <section class="card card--back" aria-label="Business card back">
    <div class="back__logo">
      <div class="brand"><span class="brand__mark"></span><span>Palm Crest</span></div>
    </div>

    <div class="back__band">
      <div class="band__arabic" lang="ar">
        <p class="person">م. سالم الفتحي بنزورة</p>
        <p>المدير العام</p>
        <p>نخيل الساحل للاستشارات والخدمات الهندسية والتدريب ذ.م.م</p>
        <p>الغربية السواني - طرابلس , ليبيا</p>
      </div>
      <div class="band__divider"></div>
      <div class="band__english">
        <p class="person">Arch. Salim Fathi Benzoura</p>
        <p>General Manager</p>
        <p>Sawani- Algharbia,</p>
        <p>District - Tripoli, Libya</p>
      </div>
    </div>

    <div class="back__contacts">
      <div class="contact">
        <svg class="contact__icon" viewBox="0 0 24 24" aria-hidden="true"><path d="M6.6 10.8a15.1 15.1 0 0 0 6.6 6.6l2.2-2.2a1 1 0 0 1 1-.25 11.4 11.4 0 0 0 3.6.57 1 1 0 0 1 1 1V20a1 1 0 0 1-1 1A17 17 0 0 1 3 4a1 1 0 0 1 1-1h3.5a1 1 0 0 1 1 1c0 1.25.2 2.45.57 3.57a1 1 0 0 1-.25 1z"/></svg>
        <span>+218215550142</span>
      </div>
      <span class="contact__sep"></span>
      <div class="contact">
        <svg class="contact__icon" viewBox="0 0 24 24" aria-hidden="true"><path d="M7 1h10a2 2 0 0 1 2 2v18a2 2 0 0 1-2 2H7a2 2 0 0 1-2-2V3a2 2 0 0 1 2-2zm0 4v13h10V5zm5 14.5a1.2 1.2 0 1 0 0 2.4 1.2 1.2 0 0 0 0-2.4z"/></svg>
        <span>+218915550187</span>
      </div>
      <span class="contact__sep"></span>
      <div class="contact">
        <svg class="contact__icon" viewBox="0 0 24 24" aria-hidden="true"><path d="M3 5h18a1 1 0 0 1 1 1v12a1 1 0 0 1-1 1H3a1 1 0 0 1-1-1V6a1 1 0 0 1 1-1zm9 7.5L4 7.4V17h16V7.4z"/></svg>
        <span>palmcrest@mailvane.net</span>
      </div>
    </div>
  </section>
</body>
</html>
```